New Interfaces

The software open with 3 open tabs, you can see the interfaces following this steps:

Brindle:
Select tab "Brindle" and click on "Brindle" in menu on the top.

KPI :
Select tab "KPI" and click on go button.

Report:
Select tab "Report" and Click on go button.

Current software: http://volteq.vextal-example.com/volteq_developers/default.aspx

user: sample_guest
pass: plinkaa

......

About the company

The VexTal is a technology company that provides planning, optimization services and software to develop the market for telecom operators.

The Product

Volteq is a web management and optimization tool for mobile networks.

The project

To always offer the best experience of usability and comfort for our customers, we are remodeling our software. The goal is to have agile, modern and with special attention to usability interfaces.

user: sample_guest
pass: plinkaa

Hi! We are analyzing all interfaces, we send news soon. Thank you!

Target Market(s)

Telecommunications Engineers.

Industry/Entity Type

Software

Font styles to use
Sans Serif

Requirements
Nice to have
• Attention for usability and good concept.
Should not have
• Many colors.

```html
<!DOCTYPE html>
<html lang="en">
<head>
<meta charset="utf-8">
<title>Brindle – Cell View</title>
<link rel="stylesheet" href="https://fonts.googleapis.com/css2?family=Arimo:wght@400;700&display=swap">
<style>
:root{
  --navy:#2b3a55;
  --heading:#33415c;
  --text:#222;
  --muted:#666;
  --line:#c8c8c8;
  --panel:#f2f2f2;
  --btn:#e4e4e4;
  --band:#dff5f7;
  --accent:#f0a545;
  --link:#1f3fae;
  --red:#e0403a;
  --menu-hi:#b9dbe6;
}
*{box-sizing:border-box;margin:0;padding:0}
html,body{width:1200px;height:617px;overflow:hidden;background:#fff;font-family:"Arimo",Arial,sans-serif;color:var(--text);font-size:11px}
.abs{position:absolute}
.topbar{left:0;top:0;width:1200px;height:25px;background:linear-gradient(#fafafa,#e6e6e6);border-bottom:1px solid var(--line)}
.search-input{left:20px;top:5px;width:106px;height:15px;background:#fff;border:1px solid #bbb}
.search-btn{left:132px;top:7px;font-size:9px;font-weight:700;color:var(--link)}
.menu{left:222px;top:1px;height:23px;width:978px;display:flex;align-items:center;border-left:1px solid var(--line);background:linear-gradient(#f7f7f7,#e2e2e2)}
.menu-item{display:flex;align-items:center;gap:4px;padding:0 7px;height:21px;font-size:10px;color:#111}
.menu-item svg{width:13px;height:13px}
.menu-item.active{background:var(--menu-hi);color:#fff;font-weight:700}
.menu-item.logoff{color:var(--link);font-weight:700}
.sidestrip{left:0;top:25px;width:20px;height:592px;background:var(--navy)}
.sidetab{position:absolute;left:0;width:20px;color:#fff;font-size:12px;writing-mode:vertical-rl;display:flex;align-items:center;justify-content:center}
.sidetab.current{background:var(--accent)}
.leftpanel{left:20px;top:25px;width:200px;height:592px;background:#fff;border-right:1px solid var(--line)}
.divider{left:221px;top:25px;width:12px;height:592px;background:var(--panel)}
.tool{position:absolute;top:5px;width:30px;height:21px;border:1px solid #bbb;border-radius:2px;background:linear-gradient(#fff,#e2e2e2);display:flex;align-items:center;justify-content:center}
.cell-title{left:12px;top:44px;font-size:13px;font-weight:700;color:var(--heading)}
.cell-title span{font-weight:400}
.attr{left:9px;width:180px;height:15px;display:flex;align-items:center;font-size:10px}
.attr .k{width:76px;height:13px;padding-left:2px;background:linear-gradient(90deg,#fff,#e8e8e8);line-height:13px}
.attr .v{padding-left:4px}
.details{left:5px;top:134px;font-size:8px;color:var(--muted)}
.section{left:9px;width:179px;font-size:13px;font-weight:700;color:var(--heading);border-bottom:1px solid var(--line);padding-bottom:2px}
.calc{position:absolute;left:164px;width:22px;height:21px;border:1px solid #bbb;border-radius:2px;background:linear-gradient(#fff,#e2e2e2);display:flex;align-items:center;justify-content:center}
.chip{position:absolute;height:17px;border:1px solid #bbb;border-radius:2px;background:var(--btn);font-size:10px;display:flex;align-items:center;justify-content:center}
.select{position:absolute;height:15px;border:1px solid #aaa;background:#fff;font-size:8px;padding-left:3px;line-height:13px;color:#888}
.select.filled{color:var(--heading);font-weight:700}
.select::after{content:"";position:absolute;right:4px;top:5px;border:4px solid transparent;border-top:4px solid #555;border-bottom:0}
.label{position:absolute;left:9px;font-size:9px;color:var(--muted)}
.main{left:233px;top:25px;width:967px;height:592px;background:#fff}
.tab{position:absolute;top:9px;height:24px;border:1px solid #ccc;border-radius:3px 3px 0 0;background:#fff;font-size:11px;color:var(--link);padding:9px 0 0 7px}
.tab.active{height:27px;color:#1f3fae}
.ic{position:absolute;width:12px;height:12px}
.btn{position:absolute;border:1px solid #bbb;border-radius:3px;background:linear-gradient(#fff,#e6e6e6);font-size:11px;display:flex;align-items:center;justify-content:center;gap:5px}
.toolbar{left:1px;top:36px;width:957px;height:25px;background:var(--band)}
.toolbar .t{position:absolute;top:7px;font-size:11px}
.date{position:absolute;top:6px;width:88px;height:14px;border:1px solid #aaa;background:#fff;font-size:9px;color:#888;padding-left:2px;line-height:12px}
.content{left:1px;top:63px;width:957px;height:529px;border:1px solid #ddd;border-bottom:none}
.info{position:absolute;left:21px;top:14px;width:915px;height:31px;background:#f7f7f7;border:1px solid #ccc;display:flex;align-items:center;padding-left:14px;font-size:11px;color:#555;gap:6px}
.info b{color:#333;font-weight:400}
.info::after{content:"";position:absolute;right:16px;top:12px;border:6px solid transparent;border-top:7px solid #666;border-bottom:0}
</style>
</head>
<body>
<header class="abs topbar">
  <div class="abs search-input"></div>
  <div class="abs search-btn">SEARCH</div>
  <nav class="abs menu">
    <div class="menu-item"><svg viewBox="0 0 12 12"><circle cx="6" cy="6" r="4" fill="none" stroke="#555" stroke-width="2"/></svg>Configuration</div>
    <div class="menu-item"><svg viewBox="0 0 12 12"><circle cx="6" cy="6" r="5" fill="#4aa54a"/><path d="M6 6V1a5 5 0 0 1 5 5z" fill="#e8a23a"/></svg>Statistics</div>
    <div class="menu-item"><svg viewBox="0 0 12 12"><rect x="2" y="1" width="8" height="10" fill="#fff" stroke="#4a78b8"/></svg>Reports</div>
    <div class="menu-item active"><svg viewBox="0 0 12 12"><rect x="1" y="1" width="10" height="10" fill="#3b6fb0"/></svg>Brindle</div>
    <div class="menu-item"><svg viewBox="0 0 12 12"><rect x="1" y="2" width="10" height="8" fill="#fff" stroke="#4a78b8"/></svg>Work Orders</div>
    <div class="menu-item"><svg viewBox="0 0 12 12"><circle cx="6" cy="6" r="5" fill="#8a5a2a"/></svg>Support</div>
    <div class="menu-item"><svg viewBox="0 0 12 12"><circle cx="6" cy="6" r="4" fill="none" stroke="#555" stroke-width="2"/></svg>Custom</div>
    <div class="menu-item"><svg viewBox="0 0 12 12"><rect x="1" y="3" width="10" height="6" fill="#999"/></svg>My View</div>
    <div class="menu-item"><svg viewBox="0 0 12 12"><circle cx="6" cy="6" r="5" fill="#3b6fb0"/></svg>Help</div>
    <div class="menu-item logoff">LogOff</div>
  </nav>
</header>

<aside class="abs sidestrip">
  <div class="sidetab" style="top:2px;height:58px">Treeview</div>
  <div class="sidetab" style="top:60px;height:78px">Workspaces</div>
  <div class="sidetab current" style="top:138px;height:60px">Brindle</div>
</aside>

<section class="abs leftpanel">
  <div class="tool" style="left:7px"><svg width="14" height="14"><circle cx="7" cy="7" r="5" fill="none" stroke="#444" stroke-width="2"/></svg></div>
  <div class="tool" style="left:42px"><svg width="14" height="14"><circle cx="7" cy="7" r="5" fill="none" stroke="#444" stroke-width="2"/><circle cx="7" cy="7" r="1.5" fill="#444"/></svg></div>
  <div class="tool" style="left:77px"><svg width="14" height="14"><path d="M4 2v10h7M4 7h7" stroke="#444" fill="none" stroke-width="1.5"/></svg></div>
  <div class="tool" style="left:112px"><svg width="14" height="14"><ellipse cx="7" cy="7" rx="6" ry="4" fill="#3b6fb0"/></svg></div>
  <div class="tool" style="left:150px"><svg width="14" height="14"><path d="M4 2l7 6-3 1 2 4-2 1-2-4-2 2z" fill="#222"/></svg></div>

  <div class="abs cell-title">UTRANCELL <span>DF0001A</span></div>
  <div class="abs attr" style="top:60px"><span class="k">LAC</span><span class="v">50161</span></div>
  <div class="abs attr" style="top:77px"><span class="k">RNC</span><span class="v">ABSA01</span></div>
  <div class="abs attr" style="top:93px"><span class="k">ScrCode</span><span class="v">243</span></div>
  <div class="abs attr" style="top:110px"><span class="k">Cell Id</span><span class="v">11</span></div>
  <div class="abs details">Show details &gt;&gt;</div>

  <div class="abs section" style="top:160px">Neighbours</div>
  <div class="calc" style="top:160px"><svg width="12" height="12"><rect x="1" y="1" width="10" height="10" fill="#555"/><rect x="3" y="3" width="6" height="2" fill="#fff"/></svg></div>
  <div class="chip" style="left:11px;top:183px;width:36px">2G</div>
  <div class="chip" style="left:51px;top:183px;width:34px">3G</div>
  <div class="chip" style="left:89px;top:183px;width:52px">3G_IF</div>

  <div class="abs section" style="top:214px">KPIs</div>
  <div class="select filled" style="left:13px;top:233px;width:163px">99_PS_INT_DELAY_DLUL_1 -...</div>

  <div class="abs section" style="top:262px">Attempts per Distance</div>
  <div class="calc" style="top:262px"><svg width="12" height="12"><rect x="1" y="1" width="10" height="10" fill="#555"/><rect x="3" y="3" width="6" height="2" fill="#fff"/></svg></div>
  <div class="chip" style="left:11px;top:280px;width:56px">PRACH</div>

  <div class="abs section" style="top:310px">Geolocation</div>
  <div class="calc" style="top:310px"><svg width="12" height="12"><rect x="1" y="1" width="10" height="10" fill="#555"/><rect x="3" y="3" width="6" height="2" fill="#fff"/></svg></div>
  <div class="label" style="top:331px">Densities</div>
  <div class="select" style="left:13px;top:343px;width:163px">Choose...</div>
  <div class="label" style="top:365px">Events</div>
  <div class="select" style="left:13px;top:377px;width:163px">Choose...</div>
  <svg class="abs" style="left:7px;top:400px" width="11" height="11"><rect x="0.5" y="0.5" width="10" height="10" fill="#fff" stroke="#d08a3a"/><rect x="2" y="2" width="7" height="3" fill="#d08a3a"/></svg>

  <div class="abs section" style="top:424px">Optimization Features</div>
  <div class="calc" style="top:425px"><svg width="12" height="12"><rect x="1" y="1" width="10" height="10" fill="#555"/><rect x="3" y="3" width="6" height="2" fill="#fff"/></svg></div>
  <div class="select" style="left:13px;top:445px;width:167px">Choose...</div>
</section>
<div class="abs divider"></div>

<main class="abs main">
  <div class="tab active" style="left:1px;width:169px">Report</div>
  <svg class="ic" style="left:129px;top:17px" viewBox="0 0 12 12"><circle cx="6" cy="6" r="5" fill="none" stroke="var(--red)"/><path d="M6 3v6M3 6h6" stroke="var(--red)"/></svg>
  <svg class="ic" style="left:149px;top:17px" viewBox="0 0 12 12"><circle cx="6" cy="6" r="5" fill="none" stroke="var(--red)"/><path d="M4 4l4 4M8 4l-4 4" stroke="var(--red)"/></svg>
  <div class="tab" style="left:175px;width:170px">KPI</div>
  <svg class="ic" style="left:306px;top:14px" viewBox="0 0 12 12"><circle cx="6" cy="6" r="5" fill="none" stroke="#e9a0a0"/><path d="M6 3v6M3 6h6" stroke="#e9a0a0"/></svg>
  <svg class="ic" style="left:324px;top:14px" viewBox="0 0 12 12"><circle cx="6" cy="6" r="5" fill="none" stroke="#e9a0a0"/><path d="M4 4l4 4M8 4l-4 4" stroke="#e9a0a0"/></svg>
  <div class="tab" style="left:350px;width:172px">Brindle</div>
  <svg class="ic" style="left:481px;top:14px" viewBox="0 0 12 12"><circle cx="6" cy="6" r="5" fill="none" stroke="#e9a0a0"/><path d="M6 3v6M3 6h6" stroke="#e9a0a0"/></svg>
  <svg class="ic" style="left:499px;top:14px" viewBox="0 0 12 12"><circle cx="6" cy="6" r="5" fill="none" stroke="#e9a0a0"/><path d="M4 4l4 4M8 4l-4 4" stroke="#e9a0a0"/></svg>
  <div class="btn" style="left:537px;top:9px;width:70px;height:23px">Tab <svg width="13" height="13" viewBox="0 0 12 12"><circle cx="6" cy="6" r="5" fill="none" stroke="#333"/><path d="M6 3v6M3 6h6" stroke="#333"/></svg></div>
  <svg class="abs" style="left:622px;top:11px" width="25" height="20"><rect x="0.5" y="0.5" width="24" height="19" fill="#fff" stroke="#d07a2a"/><rect x="3" y="3" width="19" height="14" fill="#3b6fb0"/></svg>
  <svg class="abs" style="left:655px;top:10px" width="18" height="22"><path d="M1 1h11l5 5v15H1z" fill="#fff" stroke="#c33"/><rect x="1" y="9" width="16" height="5" fill="#c33"/></svg>
  <div class="btn" style="left:686px;top:8px;width:71px;height:24px">Go All</div>

  <div class="abs toolbar">
    <svg class="ic" style="left:12px;top:7px" viewBox="0 0 12 12"><circle cx="6" cy="6" r="5" fill="none" stroke="var(--red)"/><path d="M4 4l4 4M8 4l-4 4" stroke="var(--red)"/></svg>
    <svg class="ic" style="left:31px;top:7px" viewBox="0 0 12 12"><circle cx="6" cy="6" r="5" fill="none" stroke="var(--red)"/><path d="M6 3v6M3 6h6" stroke="var(--red)"/></svg>
    <span class="t" style="left:64px">Report - Paging_3G</span>
    <div class="btn" style="left:183px;top:5px;width:40px;height:15px;font-size:9px;background:#e4e4e4">HOUR</div>
    <svg class="abs" style="left:258px;top:6px" width="14" height="14"><circle cx="7" cy="7" r="4.5" fill="none" stroke="#444" stroke-width="2.5" stroke-dasharray="2 1.5"/><circle cx="7" cy="7" r="1.5" fill="#444"/></svg>
    <span class="t" style="left:279px;top:6px">Options</span>
    <span class="t" style="left:346px">From:</span>
    <div class="date" style="left:378px">2014/05/16</div>
    <svg class="abs" style="left:449px;top:8px" width="12" height="11"><rect x="0.5" y="0.5" width="11" height="10" fill="#fff" stroke="#666"/><path d="M2 4h8M2 6.5h8M4 2v8M8 2v8" stroke="#999" stroke-width=".7"/></svg>
    <span class="t" style="left:483px">To:</span>
    <div class="date" style="left:503px">2014/05/22</div>
    <svg class="abs" style="left:574px;top:8px" width="12" height="11"><rect x="0.5" y="0.5" width="11" height="10" fill="#fff" stroke="#666"/><path d="M2 4h8M2 6.5h8M4 2v8M8 2v8" stroke="#999" stroke-width=".7"/></svg>
    <div class="btn" style="left:624px;top:6px;width:34px;height:14px;font-size:9px;background:#e4e4e4">GO</div>
  </div>

  <div class="abs content">
    <div class="info">
      <svg width="11" height="11" viewBox="0 0 12 12"><circle cx="6" cy="6" r="6" fill="#3b6fb0"/><rect x="5.2" y="5" width="1.6" height="4.5" fill="#fff"/><circle cx="6" cy="3.2" r="1" fill="#fff"/></svg>
      <span><b>Info:</b> No rows found for your request.</span>
    </div>
  </div>
</main>
</body>
</html>
```